Customize Tall Lantern Store

Hello,

I am looking to have my Tall Lantern store customized. It has the possible for simple drop-down menu changes, css-html coding, and pre-created themes. I would prefer a white background with my company icon and logo, ("What I have, what you want, and wouldn't you love to know how to get it!") included in the header. If any part of the icon is incorporated in the background, that is fine as well. I would like the store to look feminine, simple, but stylish. I only need the homepage to be unique, the other 9 pages just need what every background the homepage has. I also need a space on the homepage to write the mission statement, and it can be either on the top or the bottom.

Below are examples of Tall Lantern stores with designs I like:

mintyloveset.tall-lantern-shops.test
kolavine.tall-lantern-shops.test
parnoteck.tall-lantern-shops.test
drivelmoxa.tall-lantern-shops.test
vombrisel.tall-lantern-shops.test
plonquewearing.tall-lantern-shops.test
timandgreta.tall-lantern-shops.test
lemoulinverte.tall-lantern-shops.test
oddtrinketry.tall-lantern-shops.test
frelvo.tall-lantern-shops.test

If you have problem downloading the graphics, they are located here as well:
http://picvaultery.test/GLIMCLIENT

Industry/Entity Type

Store

Requirements
Must have
• Icon, slogan
Space to write about a paragraph of text

```html
<!DOCTYPE html>
<html lang="en">
<head>
<meta charset="utf-8">
<title>R.O.S.E — Rouge and Onyx Style Emporium</title>
<link rel="stylesheet" href="https://fonts.googleapis.com/css2?family=Bebas+Neue&family=Gelasio:wght@400&family=Parisienne&display=swap">
<style>
  :root {
    --crimson: #a3083f;
    --crimson-deep: #6b0026;
    --crimson-text: #d81e57;
    --social: #b0244f;
    --ink: #000;
    --charcoal: #1b1b1b;
    --stripe: #232323;
    --slate: #3d3d3d;
    --body-text: #9a9a9a;
    --slogan-grey: #b5b5b5;
    --white: #fff;
  }
  * { box-sizing: border-box; margin: 0; padding: 0; }
  html, body { width: 1200px; height: 1072px; overflow: hidden; }
  body {
    position: relative;
    background: repeating-linear-gradient(90deg, var(--charcoal) 0 22px, var(--stripe) 22px 44px);
    font-family: "Gelasio", Georgia, serif;
  }
  .drapes { position: absolute; inset: 0; width: 1200px; height: 1072px; }

  .store-frame {
    position: absolute; left: 163px; top: 154px; width: 878px; height: 820px;
    background: var(--crimson-deep);
  }
  .store-page {
    position: absolute; left: 186px; top: 154px; width: 832px; height: 820px;
    background: linear-gradient(180deg, #151515 0, #0a0a0a 150px, var(--ink) 260px);
  }

  .hanging-line { position: absolute; top: 0; width: 1px; height: 154px; background: #8a8a8a; }
  .hanging-line.left { left: 302px; }
  .hanging-line.right { left: 904px; }

  .brand-square { position: absolute; left: 586px; width: 28px; height: 28px; background: var(--crimson-deep); }
  .brand-square.top { top: 18px; }
  .brand-square.bottom { top: 1030px; }

  .brand { position: absolute; left: 0; width: 1200px; text-align: center; color: var(--crimson-text); font-family: "Bebas Neue", sans-serif; font-weight: 400; }
  .brand-name { top: 66px; font-size: 58px; letter-spacing: 10px; line-height: 1; }
  .brand-tagline { top: 126px; font-size: 19px; letter-spacing: 5px; line-height: 1; }

  .social { position: absolute; top: 128px; left: 922px; display: flex; gap: 10px; }
  .social a { color: var(--social); font-family: "Bebas Neue", sans-serif; font-size: 17px; line-height: 20px; letter-spacing: 1px; text-decoration: none; }

  .main-nav {
    position: absolute; left: 186px; top: 154px; width: 832px; height: 48px;
    background: linear-gradient(180deg, #2e2e2e, #121212);
    display: flex; justify-content: center; align-items: center;
  }
  .main-nav a {
    color: var(--crimson-text); font-family: "Bebas Neue", sans-serif; font-size: 21px;
    letter-spacing: 0.5px; text-decoration: none; padding: 0 24px; line-height: 24px;
    border-left: 1px solid #3c3c3c;
  }
  .main-nav a:first-child { border-left: 0; }

  .slogan {
    position: absolute; left: 186px; top: 220px; width: 832px; text-align: center;
    font-family: "Parisienne", cursive; font-size: 33px; line-height: 42px; color: var(--slogan-grey);
  }
  .slogan em { font-style: normal; color: var(--crimson-text); }

  .section-title {
    position: absolute; font-family: "Bebas Neue", sans-serif; font-weight: 400;
    color: var(--crimson-text); font-size: 33px; line-height: 1;
  }
  .mission-title { left: 224px; top: 328px; }
  .popular-title { left: 221px; top: 668px; }

  .mission-text { position: absolute; left: 224px; top: 361px; width: 755px; color: var(--body-text); font-size: 12.4px; line-height: 20.8px; }
  .mission-text p + p { margin-top: 20.8px; }

  .product-card { position: absolute; top: 702px; width: 131px; height: 222px; background: var(--crimson); }
  .product-photo {
    position: absolute; left: 5px; top: 6px; width: 121px; height: 184px;
    background: linear-gradient(180deg, #e9e9e9 0%, #9b9ea3 45%, #b7202c 70%, #9ea1a6 100%);
  }
  .product-price {
    position: absolute; left: 0; bottom: 0; width: 131px; height: 27px;
    background: #4e001b; color: var(--white); text-align: center; font-size: 15px; line-height: 27px;
  }

  .copyright { position: absolute; left: 0; top: 985px; width: 1200px; text-align: center; color: #8c8c8c; font-size: 9.5px; }
</style>
</head>
<body>
  <svg class="drapes" viewBox="0 0 1200 1072" aria-hidden="true">
    <path d="M0,0H1200V125C1010,118 800,128 600,175C400,128 190,118 0,125Z" fill="#141414"/>
    <path d="M0,0H1200V92C1040,98 840,70 600,150C360,70 160,98 0,92Z" fill="var(--crimson-deep)"/>
    <path d="M0,0H1200V80C1060,84 880,30 600,95C320,30 140,84 0,80Z" fill="var(--crimson)"/>
    <path d="M0,0H1200V48C1060,60 880,0 640,0H560C320,0 140,60 0,48Z" fill="#262626"/>
    <path d="M0,0H1200V20C1080,26 900,0 760,0H440C300,0 120,26 0,20Z" fill="var(--slate)"/>
  </svg>

  <span class="hanging-line left"></span>
  <span class="hanging-line right"></span>
  <span class="brand-square top"></span>

  <header>
    <div class="brand brand-name">R.O.S.E</div>
    <div class="brand brand-tagline">Rouge and Onyx Style Emporium</div>
    <nav class="social">
      <a href="#">Chirp</a>
      <a href="#">Folks</a>
      <a href="#">Pixlo</a>
    </nav>
  </header>

  <div class="store-frame"></div>
  <main class="store-page"></main>

  <nav class="main-nav">
    <a href="#">Tops</a>
    <a href="#">Bottoms</a>
    <a href="#">Accessories</a>
    <a href="#">Clearance</a>
    <a href="#">What's New</a>
    <a href="#">Contact Us</a>
  </nav>

  <p class="slogan">What I <em>have</em>, What you <em>want</em>,<br>And wouldn't you <em>love</em> to know how to <em>get it!</em></p>

  <h2 class="section-title mission-title">Mission Statement</h2>
  <div class="mission-text">
    <p>Lorem ipsum dolor sit amet, consectetur adipiscing elit. Ut pharetra augue ut sem volutpat tempor. In facilisis laoreet egestas. Curabitur bibendum vestibulum posuere. Sed sit amet dui id dui molestie faucibus. Donec turpis sem, facilisis sit amet vestibulum quis, aliquet a ante. Pellentesque habitant morbi tristique senectus et netus et malesuada fames ac turpis egestas. Etiam lacinia congue odio, ultricies luctus elit pellentesque in. Aenean venenatis elit ac metus vulputate a rhoncus nunc molestie. Sed ut orci justo. Ut vitae convallis ligula. Cras et odio erat. Etiam eget odio et ipsum convallis laoreet. Nullam dictum, felis vel euismod pretium, purus ipsum convallis lorem, ac sagittis urna orci accumsan leo. Vestibulum at est eros.</p>
    <p>Donec sed elit velit. Aenean facilisis velit id nisi pharetra elementum. Donec blandit mauris vitae libero fringilla ultrices. Suspendisse eu turpis eget nulla cursus dictum. Sed mauris elit, gravida sed adipiscing vel, rutrum ut massa. Vivamus fermentum, arcu non lobortis condimentum, diam mauris aliquam ligula, sed iaculis orci nisl a risus. Integer auctor eleifend elit nec tincidunt. Sed tempor quam iaculis lacus ultrices facilisis. Fusce auctor molestie vestibulum. Proin ullamcorper diam quis nisi auctor mattis id sagittis dolor. Vestibulum ultricies, purus a scelerisque ultrices, risus dui luctus nunc, nec pellentesque elit magna non felis. Morbi tristique urna vel arcu varius scelerisque.</p>
  </div>

  <h2 class="section-title popular-title">Popular</h2>
  <article class="product-card" style="left:221px">
    <div class="product-photo" role="img" aria-label="Product photo: model in a grey hoodie with a red lips print"></div>
    <div class="product-price">$25.00</div>
  </article>
  <article class="product-card" style="left:429px">
    <div class="product-photo" role="img" aria-label="Product photo: model in a grey hoodie with a red lips print"></div>
    <div class="product-price">$25.00</div>
  </article>
  <article class="product-card" style="left:637px">
    <div class="product-photo" role="img" aria-label="Product photo: model in a grey hoodie with a red lips print"></div>
    <div class="product-price">$25.00</div>
  </article>
  <article class="product-card" style="left:844px">
    <div class="product-photo" role="img" aria-label="Product photo: model in a grey hoodie with a red lips print"></div>
    <div class="product-price">$25.00</div>
  </article>

  <svg class="drapes" viewBox="0 0 1200 1072" aria-hidden="true">
    <path d="M0,985C220,980 420,955 600,950C780,955 980,980 1200,985V1072H0Z" fill="var(--crimson-deep)"/>
    <path d="M0,990C200,1000 420,990 600,1040C780,990 1000,1000 1200,990V1072H0Z" fill="var(--crimson)"/>
    <path d="M0,1030C200,1040 420,1020 600,1068C780,1020 1000,1040 1200,1030V1072H0Z" fill="#262626"/>
    <path d="M0,1055C220,1060 440,1050 560,1072H640C760,1050 980,1060 1200,1055V1072H0Z" fill="var(--slate)"/>
  </svg>

  <footer class="copyright">Copyright 2011-2012 Lorem Ipsum. All rights reserved.</footer>
  <span class="brand-square bottom"></span>
</body>
</html>
```